Rings and things/plans. Wedding planning checklist design

We are a wedding videography start-up that's about to launch a chatterly campaign. We need a simple yet premium looking design to showcase a wedding planning checklist which we have written. The main focus of the design should be:

- On A4 pages
- Appeal to young engaged women
- Anyone at home can print it off and stick it onto a fridge
- Premium looking

The contents doesn't have to be on one piece of A4, the list can span more than one page. Also, it doesn't have to be traditional folded brochure style, a full A4 sized list is preferred. The design will potentially be used in further A4 brochure style blog posts. The written checklist and our company logo is attached for reference.

Target Market(s)

Young engaged woman

Industry/Entity Type

Wedding

Requirements
Must have
• Simple and premium feel.
Nice to have
• flexible design that can be reused in the future for blog posts.

```html
<!DOCTYPE html>
<html lang="en">
<head>
<meta charset="utf-8">
<title>Wedding Planning Checklist</title>
<link href="https://fonts.googleapis.com/css2?family=Crimson+Text:wght@400;700&family=Raleway:wght@300;400&family=Pacifico&family=Kaushan+Script&display=swap" rel="stylesheet">
<style>
  :root {
    --backdrop: #2f2f31;
    --paper: #ffffff;
    --ink: #2b2b2b;
    --ink-soft: #555555;
    --accent: #c8102e;
    --band-peach: #f3dcd4;
    --band-rose: #f2dde1;
    --photo-warm: #e9b9a2;
    --photo-light: #fbeee6;
  }
  * { box-sizing: border-box; margin: 0; padding: 0; }
  html, body { width: 1200px; height: 900px; overflow: hidden; }
  body { background: var(--backdrop); position: relative; }

  .sheet {
    position: absolute; left: 296px; top: 20px;
    width: 608px; height: 860px;
    background: var(--paper);
    overflow: hidden;
    box-shadow: 0 10px 30px rgba(0,0,0,.45);
  }

  .hero-photo {
    position: absolute; left: 0; top: 0; width: 330px; height: 470px;
    background:
      radial-gradient(ellipse at 40% 35%, var(--photo-warm) 0%, rgba(233,185,162,.6) 40%, rgba(255,255,255,0) 75%),
      linear-gradient(180deg, var(--photo-light), rgba(255,255,255,0));
  }

  .masthead {
    position: absolute; left: 250px; right: 20px; top: 40px;
    text-align: center; color: var(--ink);
  }
  .brand {
    font-family: "Raleway", sans-serif; font-weight: 400;
    font-size: 22px; letter-spacing: 0;
    color: var(--ink);
  }
  .title-rule {
    display: flex; align-items: center; gap: 12px; justify-content: center;
    font-family: "Raleway", sans-serif; font-weight: 300; font-size: 21px;
  }
  .title-rule::before, .title-rule::after {
    content: ""; flex: 1; height: 1px; background: var(--ink);
  }
  .title-rule.upper { margin-top: 30px; }
  .title-main {
    font-family: "Pacifico", cursive; font-weight: 400; color: var(--accent);
    font-size: 32px; line-height: 1.4;
  }
  .tagline {
    margin-top: 22px;
    font-family: "Raleway", sans-serif; font-weight: 400;
    color: var(--accent); font-size: 26px;
  }

  .timeline-rule {
    position: absolute; left: 70px; top: 290px; bottom: 20px;
    width: 1.5px; background: var(--accent);
  }
  .phase-label {
    position: absolute; left: 22px; top: 440px;
    transform: rotate(-90deg); transform-origin: left top;
    font-family: "Kaushan Script", cursive; color: var(--accent);
    font-size: 38px; line-height: 1; white-space: nowrap;
  }

  .checklist {
    position: absolute; left: 71px; right: 0; top: 285px;
    list-style: none;
  }
  .task {
    display: flex; align-items: center;
    height: 55px; padding: 0 20px;
  }
  .task:nth-child(odd) { background: var(--band-peach); }
  .task:nth-child(odd):nth-child(n+5) { background: var(--band-rose); }
  .task-name {
    width: 245px; padding-left: 12px;
    font-family: "Crimson Text", serif; font-weight: 700;
    font-size: 15px; line-height: 1.15; color: var(--ink);
  }
  .task-note {
    flex: 1;
    font-family: "Crimson Text", serif; font-weight: 400;
    font-size: 11.5px; line-height: 1.2; color: var(--ink-soft);
  }
</style>
</head>
<body>
  <main class="sheet">
    <div class="hero-photo" role="img" aria-label="Soft, sunlit photo of a smiling bride in a veil, fading into the page"></div>

    <header class="masthead">
      <p class="brand">Bloomline Films</p>
      <p class="title-rule upper">The Ultimate</p>
      <h1 class="title-main">Wedding Planning</h1>
      <p class="title-rule">Checklist</p>
      <p class="tagline">Rings and plans!</p>
    </header>

    <div class="timeline-rule"></div>
    <p class="phase-label">12 Months</p>

    <ul class="checklist">
      <li class="task"><span class="task-name">Decide on a date and venue</span><span class="task-note">The earlier you can reserve these, the better! Will it be a church, garden or beach wedding?</span></li>
      <li class="task"><span class="task-name">Organise a meeting of the parents and determine your budget</span><span class="task-note">Work out how much each family is contributing so that there are no surprises</span></li>
      <li class="task"><span class="task-name">Choose the type of wedding</span><span class="task-note">Form a basic idea of the kind of wedding you would like to have e.g.- simple or lavish?</span></li>
      <li class="task"><span class="task-name">Pick your wedding party</span><span class="task-note">Best man, groomsmen, maid of honor, bridesmaids, flower girl, ring bearer etc.</span></li>
      <li class="task"><span class="task-name">Pick or hire a MC</span><span class="task-note">Someone who enjoys being in the limelight, is confident telling a few jokes, and will make sure everyone is having a good time</span></li>
      <li class="task"><span class="task-name">Start a wedding folder</span><span class="task-note">This is where you can compile your notes and ideas about anything wedding related</span></li>
      <li class="task"><span class="task-name">Hire a planner</span><span class="task-note">A planner will take the stress off you and they can negotiate good deals with vendors</span></li>
      <li class="task"><span class="task-name">Start your guest list</span><span class="task-note">Be realistic about the number of guests to avoid stress later on</span></li>
      <li class="task"><span class="task-name">Research your wedding professionals (vendors?)</span><span class="task-note">These include your videographers, photographers, caterer, DJ, florist, decorator etc. Wedding planners can help with this!</span></li>
      <li class="task"><span class="task-name">Start shopping for wedding rings and your dress</span><span class="task-note">The sooner you buy them, the sooner you can check it off your list</span></li>
    </ul>
  </main>
</body>
</html>
```